Flyer to promote new Commercial HVAC Preventative Maintenance clients

This flyer will be in the body of emails that will be sent to new, existing, and/or potential commericial buildings HVAC clients. It will have the least amount of words used, but it will convey the point with pertinent pictorial and graphics. It will show the value of a Periodic/Preventative routine maintenance to lower operating costs of their commericial buildings (i.e. office, medical, shopping centers, apartment, warehouse facility, etc.), in the following ways:
1) Reduce monthly power usage,
2) Reduce emergency HVAC service calls,
3) Reduce costly repairs costs,
4) Reduce HVAC down-times and angry tenants,
5) Increases the life expectancy of the existing and/or new HVAC equipment in the building and/or the equipment's' early replacement costs,
6) Reduces tenant's early termination of their lease and law suits against the landlords,
7) Increases tenant's renewal of the lease and agree to pay the increase rental rates,
8) Reduces unhappy customers and increases tenant's productivity,
9) By reducing the landlord's expenses, the value of the property will increase considerably and profitable to sell their holdings, or refinance and keep their holdings with an increased ROI (Return On Investment).

Landlords can not depend on their tenants' obligation to maintain the landlords' major assets, which is their HVAC equipment and systems.

With the periodic maintenance done by one reliable and licensed HVAC company, the will not use different companies that may or may not do the right repair job on their unit and hurt their bottom line and increase HVAC replacement COSTLY rates.

```html
<!DOCTYPE html>
<html lang="en">
<head>
<meta charset="utf-8">
<title>Commercial HVAC Preventative Maintenance Flyer</title>
<link href="https://fonts.googleapis.com/css2?family=Montserrat:wght@400;500;600;700;800&display=swap" rel="stylesheet">
<style>
  :root {
    --navy: #1b3a72;
    --navy-deep: #163063;
    --orange: #ef8a22;
    --ink: #333a45;
    --white: #ffffff;
    --photo-warm: #c9633a;
    --photo-steel: #c8ccd2;
  }
  * { margin: 0; padding: 0; box-sizing: border-box; }
  html, body { width: 871px; height: 1200px; overflow: hidden; background: var(--white); }
  body { font-family: 'Montserrat', sans-serif; }
  .flyer { position: relative; width: 871px; height: 1200px; overflow: hidden; background: var(--white); }

  /* Hero */
  .hero { position: absolute; left: 0; top: 0; width: 871px; height: 355px; background: var(--white); }
  .hero-photo {
    position: absolute; right: 0; top: 0; width: 560px; height: 355px;
    background:
      linear-gradient(90deg, rgba(255,255,255,1) 0%, rgba(255,255,255,0.75) 25%, rgba(255,255,255,0) 55%),
      radial-gradient(ellipse at 85% 55%, var(--photo-warm) 0%, #8a4a2e 30%, transparent 55%),
      linear-gradient(120deg, #eef0f2 0%, var(--photo-steel) 45%, #6b6f75 80%, #3b3d40 100%);
  }
  .brand {
    position: absolute; left: 41px; top: 80px;
    font-weight: 800; font-size: 34px; letter-spacing: -0.5px; color: var(--navy);
  }
  .headline { position: absolute; left: 41px; top: 148px; color: var(--orange); font-size: 37px; line-height: 47px; }
  .headline strong { font-weight: 800; display: block; }
  .headline span { font-weight: 500; display: block; }
  .subhead { position: absolute; left: 41px; top: 249px; font-size: 19.5px; line-height: 30px; color: var(--ink); font-weight: 400; }

  /* Benefits */
  .benefits { position: absolute; left: 0; top: 355px; width: 871px; height: 554px; background: var(--navy); }
  .benefits-bg {
    position: absolute; inset: 0;
    background:
      radial-gradient(circle at 33% 37%, rgba(255,255,255,0.04) 0, rgba(255,255,255,0.04) 85px, transparent 86px),
      radial-gradient(circle at 58% 37%, rgba(255,255,255,0.04) 0, rgba(255,255,255,0.04) 85px, transparent 86px),
      radial-gradient(circle at 80% 37%, rgba(255,255,255,0.04) 0, rgba(255,255,255,0.04) 85px, transparent 86px),
      linear-gradient(180deg, var(--navy) 0%, var(--navy-deep) 100%);
  }
  .benefits-title {
    position: absolute; top: 27px; left: 0; width: 100%; text-align: center;
    color: var(--white); font-weight: 700; font-size: 24px; line-height: 30px;
  }
  .benefits-title em { font-style: normal; color: var(--orange); }
  .benefit { position: absolute; width: 300px; text-align: center; color: var(--white); }
  .benefit svg { display: block; margin: 0 auto; width: 50px; height: 50px; }
  .benefit p { margin-top: 14px; font-size: 15.5px; line-height: 19.6px; font-weight: 400; }
  .col-1 { left: 15px; }
  .col-2 { left: 291px; }
  .col-3 { left: 571px; }
  .row-1 { top: 82px; }
  .row-2 { top: 223px; }
  .row-3 { top: 398px; }
</style>
</head>
<body>
<div class="flyer">

  <header class="hero">
    <div class="hero-photo" role="img" aria-label="Technician in orange work wear checking refrigerant pressure gauges on a commercial HVAC unit"></div>
    <div class="brand">COREFLOW HVAC</div>
    <h1 class="headline"><strong>Unlock Savings,</strong><span>Ensure Sustainability</span></h1>
    <p class="subhead">Elevate Your Commercial Building's<br>Efficiency with Periodic Maintenance!</p>
  </header>

  <section class="benefits">
    <div class="benefits-bg" role="img" aria-label="Faded photo of rooftop condenser fans in navy tint"></div>
    <h2 class="benefits-title">Benefits of <em>Preventative Maintenance</em></h2>

    <div class="benefit col-1 row-1">
      <svg viewBox="0 0 54 54" fill="none" stroke="#fff" stroke-width="2" stroke-linecap="round" stroke-linejoin="round">
        <circle cx="24" cy="22" r="18"/><path d="M27 10 L19 24 H26 L22 34 L31 19 H24 Z"/><path d="M8 36 L18 44 L28 38 L44 50"/><path d="M38 50 H44 V44"/>
      </svg>
      <p>Reduce monthly<br>power usage</p>
    </div>
    <div class="benefit col-2 row-1">
      <svg viewBox="0 0 54 54" fill="none" stroke="#fff" stroke-width="2" stroke-linecap="round" stroke-linejoin="round">
        <circle cx="34" cy="18" r="15"/><path d="M8 26 C4 34 12 46 22 50 L26 46 L20 40 L16 42 C13 38 12 35 13 32 L17 30 L14 22 Z"/>
      </svg>
      <p>Reduce emergency<br>HVAC service calls</p>
    </div>
    <div class="benefit col-3 row-1">
      <svg viewBox="0 0 54 54" fill="none" stroke="#fff" stroke-width="2" stroke-linecap="round" stroke-linejoin="round">
        <path d="M27 4 L31 9 L37 7 L38 13 L44 15 L42 21 L47 26 L42 31 L44 37 L38 39 L37 45 L31 43 L27 48 L23 43 L17 45 L16 39 L10 37 L12 31 L7 26 L12 21 L10 15 L16 13 L17 7 L23 9 Z"/>
        <path d="M31 19 C29 17 23 17 23 21 C23 25 31 24 31 29 C31 33 25 33 23 31 M27 14 V36"/><path d="M42 34 V48 M37 43 L42 48 L47 43"/>
      </svg>
      <p>Reduce costly<br>repairs costs</p>
    </div>

    <div class="benefit col-1 row-2" style="left:9px;">
      <svg viewBox="0 0 54 54" fill="none" stroke="#fff" stroke-width="2" stroke-linecap="round" stroke-linejoin="round">
        <path d="M8 30 A20 20 0 0 1 44 14"/><path d="M46 24 A20 20 0 0 1 14 44"/><path d="M20 20 C20 14 34 14 34 20 L36 34 H18 Z"/>
        <path d="M29 22 C28 20 24 20 24 23 C24 26 30 25 30 28 C30 31 25 31 24 29 M27 19 V33"/><path d="M8 40 H22 L28 36"/>
      </svg>
      <p>Lower Expenses,<br>Increase Property Value,<br>Maximize ROI<br>(Return On Investment)</p>
    </div>
    <div class="benefit col-2 row-2">
      <svg viewBox="0 0 54 54" fill="none" stroke="#fff" stroke-width="2" stroke-linecap="round" stroke-linejoin="round">
        <path d="M8 16 L27 8 L46 16 V40 L27 48 L8 40 Z"/><path d="M8 16 L27 24 L46 16 M27 24 V48"/>
        <path d="M12 24 L23 29 M12 30 L23 35 M12 36 L23 41 M31 29 L42 24 M31 35 L42 30 M31 41 L42 36"/>
      </svg>
      <p>Boosts HVAC lifespan<br>of the existing and/or<br>new HVAC equipment, Cut<br>early replacement Costs!</p>
    </div>
    <div class="benefit col-3 row-2">
      <svg viewBox="0 0 54 54" fill="none" stroke="#fff" stroke-width="2" stroke-linecap="round" stroke-linejoin="round">
        <path d="M12 6 H32 L40 14 V48 H12 Z"/><path d="M32 6 V14 H40"/><path d="M18 24 H34 M18 30 H30 M18 36 H26"/><path d="M22 18 L22 12 M19 15 L22 12 L25 15"/>
        <path d="M30 42 L46 26 L50 30 L34 46 L29 47 Z"/>
      </svg>
      <p>Reduces tenant's early<br>termination of their<br>lease and law suits<br>against the landlords</p>
    </div>

    <div class="benefit col-1 row-3">
      <svg viewBox="0 0 54 54" fill="none" stroke="#fff" stroke-width="2" stroke-linecap="round" stroke-linejoin="round">
        <path d="M4 16 L17 6 L30 16"/><path d="M8 14 V48 H24"/><path d="M12 20 H24 M12 26 H24 M12 32 H22"/><path d="M12 48 V38 H18 V48"/>
        <circle cx="36" cy="38" r="12"/><path d="M28 36 A8 8 0 0 1 42 32 M44 40 A8 8 0 0 1 30 44"/>
      </svg>
      <p>Increases tenant's renewal<br>of the lease and agree to<br>pay the increase rental rates</p>
    </div>
    <div class="benefit col-2 row-3">
      <svg viewBox="0 0 54 54" fill="none" stroke="#fff" stroke-width="2" stroke-linecap="round" stroke-linejoin="round">
        <circle cx="22" cy="24" r="9"/><path d="M16 14 L18 8 L22 12 L26 8 L28 14"/>
        <path d="M6 50 V44 C6 38 12 35 22 35 C32 35 38 38 38 44 V50 Z"/><path d="M40 4 V18 M36 14 L40 18 L44 14"/><path d="M46 10 V24 M42 20 L46 24 L50 20"/>
      </svg>
      <p>Reduces unhappy<br>customers and increases<br>tenant's productivity</p>
    </div>
    <div class="benefit col-3 row-3">
      <svg viewBox="0 0 54 54" fill="none" stroke="#fff" stroke-width="2" stroke-linecap="round" stroke-linejoin="round">
        <path d="M44 18 A20 20 0 1 0 46 32"/><path d="M38 16 L45 19 L48 12"/><circle cx="26" cy="27" r="14"/><path d="M26 19 V27 L32 31"/>
      </svg>
      <p>Reduce HVAC down-times<br>and angry tenants</p>
    </div>
  </section>

  <section class="trust" style="position:absolute; left:0; top:909px; width:871px; height:200px; background:var(--white);">
    <div class="trust-photo" style="position:absolute; left:0; top:0; width:395px; height:200px; background:linear-gradient(170deg, #8fa9c4 0%, #b9c7d6 40%, #d8dde3 65%, #9ea7b1 100%);" role="img" aria-label="Rooftop commercial air conditioning condenser units on a concrete pad"></div>
    <p class="trust-copy" style="position:absolute; left:425px; top:33px; width:440px; font-size:22px; line-height:34px; font-weight:700; color:var(--navy);">Trust a Reliable, Licensed HVAC<br>Partner for <em style="font-style:normal; color:var(--orange);">Periodic Maintenance.</em><br><em style="font-style:normal; color:var(--orange);">Avoid Costly Repairs</em> and<br>Ensure Longevity.</p>
  </section>

  <footer class="footer" style="position:absolute; left:0; top:1109px; width:871px; height:91px;">
    <svg style="position:absolute; left:0; top:0; width:871px; height:91px;" viewBox="0 0 871 91" preserveAspectRatio="none" aria-hidden="true">
      <polygon points="520,25 871,25 871,91 555,91" fill="#1b3a72"/>
      <polygon points="0,0 505,0 552,91 0,91" fill="#ef8a22"/>
    </svg>
    <div style="position:absolute; left:53px; top:24px; font-size:33px; line-height:40px; color:var(--white); font-weight:400;">www.<b style="font-weight:700;">yourwebsite</b>.com</div>
    <div style="position:absolute; left:575px; top:38px; display:flex; align-items:center; gap:12px; color:var(--white); font-weight:700; font-size:29px; line-height:36px;">
      <svg style="width:26px; height:26px;" viewBox="0 0 26 26" fill="none" stroke="#fff" stroke-width="2.2" stroke-linecap="round" stroke-linejoin="round">
        <path d="M5 3 L9 3 L11 8 L8 10 C9 13 12 16 15 17 L17 14 L22 16 L22 20 C22 22 20 23 18 23 C10 22 4 16 3 8 C3 6 4 3 5 3 Z"/>
        <path d="M15 3 A8 8 0 0 1 23 11 M15 7 A4 4 0 0 1 19 11"/>
      </svg>
      <span>123 456 7890</span>
    </div>
  </footer>

</div>
</body>
</html>
```